Wealth Education Business Needs Sharp Business Card Design

We need a business card design for a recently launched investor education business called Harbor Ledger.

The final design should promote security, empowerment, self improvement and financial gain. The card will ideally promote the stature of the business.

For more information and colours please visit harborledger-example.com.au

Target Market(s)

Corporate executives and high net worth individuals

Industry/Entity Type

Education

Contact Information for Business Card

Name
Position
Contact Address
Phone
Mobile
Email
Website

```html
<!DOCTYPE html>
<html lang="en">
<head>
<meta charset="utf-8">
<title>Harbor Ledger – Business Card</title>
<link rel="stylesheet" href="https://fonts.googleapis.com/css2?family=Open+Sans:wght@400;600;700&family=Oswald:wght@500&display=swap">
<style>
  :root {
    --navy: #1c2a3d;
    --paper: #e5e6e8;
    --stage: #d9dadc;
    --teal: #1e9a9c;
    --name-grey: #8c8d8f;
    --ink: #1f2226;
    --white: #ffffff;
  }
  * { box-sizing: border-box; margin: 0; padding: 0; }
  html, body {
    width: 1200px; height: 900px; overflow: hidden;
    background: var(--stage);
    font-family: "Open Sans", Arial, sans-serif;
  }
  .stage {
    width: 1200px; height: 900px;
    display: flex; align-items: center; justify-content: center; gap: 60px;
  }
  .card {
    width: 380px; height: 620px;
    border-radius: 22px; overflow: hidden;
    position: relative;
    box-shadow: 0 6px 18px rgba(0,0,0,0.18);
  }
  /* Front */
  .card-front { background: var(--paper); display: flex; flex-direction: column; }
  .front-head {
    height: 232px; background: var(--navy);
    display: flex; align-items: center; justify-content: center;
    position: relative;
  }
  .front-head .pointer {
    position: absolute; bottom: -16px; left: 50%; transform: translateX(-50%);
  }
  .brand {
    display: flex; align-items: center; gap: 12px;
    color: var(--white);
    font-family: "Open Sans", Arial, sans-serif;
    font-weight: 700; letter-spacing: 2px; text-transform: uppercase;
    white-space: nowrap;
  }
  .brand-square { background: var(--teal); flex: none; }
  .front-head .brand { font-size: 27px; }
  .front-head .brand-square { width: 22px; height: 22px; }
  .front-body {
    flex: 1; text-align: center; color: var(--ink);
    padding-top: 44px;
  }
  .person-name {
    font-family: "Oswald", "Arial Narrow", sans-serif;
    font-weight: 500; font-size: 31px; line-height: 1; letter-spacing: 0.5px;
  }
  .person-name .first { color: var(--teal); }
  .person-name .last { color: var(--name-grey); }
  .person-role { font-size: 15px; margin-top: 4px; }
  .address { font-size: 15px; line-height: 1.35; margin-top: 38px; }
  .phones { font-size: 15px; line-height: 1.6; margin-top: 24px; }
  .email { font-size: 15px; margin-top: 18px; white-space: nowrap; }
  .front-foot {
    height: 78px; background: var(--navy); color: var(--white);
    display: flex; align-items: center; justify-content: center;
    font-size: 17px; font-weight: 600; letter-spacing: 0.3px;
    white-space: nowrap;
  }
  /* Back */
  .card-back {
    background: var(--navy);
    display: flex; align-items: center; justify-content: center;
  }
  .card-back .brand { font-size: 24px; }
  .card-back .brand-square { width: 20px; height: 20px; }
</style>
</head>
<body>
  <main class="stage">
    <article class="card card-front">
      <header class="front-head">
        <div class="brand"><span class="brand-square"></span>Harbor Ledger</div>
        <svg class="pointer" width="32" height="17" viewBox="0 0 32 17" aria-hidden="true">
          <polygon points="0,0 32,0 16,16" fill="var(--navy)"/>
        </svg>
      </header>
      <section class="front-body">
        <h1 class="person-name"><span class="first">YOUR</span> <span class="last">NAME</span></h1>
        <p class="person-role">Position</p>
        <p class="address">Level 4, 72 Quayside Walk<br>Melbourne VIC 3000</p>
        <p class="phones">T: 1300 555 014<br>M: +613 5550 2947</p>
        <p class="email">E: support@harborledger-example.com.au</p>
      </section>
      <footer class="front-foot">www.harborledger-example.com.au</footer>
    </article>

    <article class="card card-back">
      <div class="brand"><span class="brand-square"></span>Harbor Ledger</div>
    </article>
  </main>
</body>
</html>
```